Tradeshow Booth, Banners & Brochure Design

Corvin Meridian (www.corvinmeridian.example) is a Veltrax Partner specializing in developing products and customizations for Veltrax Ledgerline QP. The purpose of this project is to develop a unified approach to graphic design for our tradeshow booth, banners and product literature. This should result in completed designs for the booth and banners, and several templates that can be used to create our product literature.

***WE WILL ONLY LOOK THROUGH THE FIRST 100 SUBMISSIONS***
Updates

Reason: We have received some requests for an extended deadline, and we would like to encourage more submissions, so we are extending the deadline by two days. Please let us know if you have any questions or need clarification on our design brief.

Thanks for the submissions and questions everyone.  I will get answers to your questions, and more detailed specs, posted within the next couple of hours.  I will also provide detailed feedback to your designs within that time.

Q:  How large should each item be – what is the approximate number of words/lines, columns/rows?

 

-          We have updated the Content Type list to cut it down and simplify this.  For word count, we are attaching the text for our NEW brochure on WMS, which we intend to be a 4 page brochure.  We have labeled each section according to content type.  This can be used as a guide for how much text each content area must be able to accommodate.  You can even pull the raw text straight from the word file for your design.  The CCEM brochure, already included, is an OLD brochure, and represents a design that we are trying to evolve beyond.

 

-          Keep in mind that the 4 page product brochure will be a 17” by 11” single sheet, folded.  The 2 page product brochure will be a single 8.5” by 11” sheet, printed on both sides.

 

-          For the 2 page product brochure, assume something that looks like half of the 4 page design.  For example, we will be creating one brochure for “Financials” which comprises two products.  Product A will go on the front, and Product B on the back.  We will still need to allow for contact information and the other content types as specified.

 

-          For the 4 page corporate overview, we have attached our current corporate overview for reference, and labeled the content types.  Again, feel free to pull raw text directly from this for purposes of your design – though remember, this OLD brochure represents a design we are trying to evolve beyond.

 

-          For images (screenshots, stock photography, diagrams, etc) we are thinking we would like to see about 4 on the 4 page brochure, but only 1-2 for the 2 page brochure.  The corporate overview can have suitable imagery at your discretion.

 

-          We would like to see some of the imagery used in the Tradeshow materials (booth, banners) carried across to the brochures.

 

 

 

Q:  What are the detailed print guidelines, especially in relation to bleeds, etc?

 

-          For all the brochures, use a full bleed.  If your design incorporates a bleed of color across a fold, try to have the bleed going across no more than 25% of the height of the page.  CMYK color, 300DPI, 8.5”w x 11”h.  We will most likely go with 100# paper without too much gloss on it. 

 

-          For all other materials such as booth and banners, no bleeds.  Please see specification sheets for the booth and banners, included below.  Create your designs to the exact size given.

 

 

 

Q:  Will booth graphics be printed as one continuous piece, or will they be applied in sections that are in line with the panel dimensions of the 8 center panels and end caps?

 

-          Graphics are printed as one continuous piece on a large format printer.  They are then cut into the individual panel pieces for shipping and storage.  When the booth is fully assembled, the seams are hardly noticeable unless you are looking for them from a short distance away.

 

-          We are already in possession of one 10’ booth, and will be ordering another, with the associated pieces, to create the 20’ booth.  The booth comprises a support structure, and the actual graphics panels which are attached to the front.  The overall 20’ design should take into account the fact that we will, in the future, attend tradeshows with only a 10’ booth, so only half of the panels will be used.  We would like to be able to mix and match our four categories to suit the show.

Reason: We are extending the deadline one more time to allow Tamsin and anyone else who needs the extra time for the brochure design.

Please prioritize your brochure design at this time.  We are interested in receiving feedback on deadlines - if you can confirm that you will submit a design but need more time to do so, we would like to hear from you.

Reason: To provide time for solid designs from all the designers who have been invited, we are extended the deadline one more time. This will be the final extension.

Target Market(s)

Corporate Clients

Industry/Entity Type

Graphic Design

Requirements
Must have
• TRADESHOW SPECIFIC
1. Graphics for 10'x20' “Heronfold” Tradeshow Booth
a. Layout should approximate the grid we have mocked up in our preliminary layout – see below. There is a fair amount of flexibility so long as the basic grid, contents and dimensions are adhered to.

2. Graphics needed for 3 retractable banner stands
a. Two banner stands will have dimensions of 24” x 88”
b. The third banner stand will have dimensions of 36” x 88” and will be double-sided. The design for this banner should have the option to be scaled down to 33.5” wide, for a possible additional banner stand being considered.
c. Banners should approximate what is shown in the preliminary layout – see below.
d. All banner stands being used are able to fully extend to 92”- however, the height of the booth itself is 88” and we would like all tradeshow specific elements to be the same height.

PRODUCT LITERATURE
1. Graphic Design and Layout needed for brochures:
a. double-sided one page for Products
b. double-sided two page for Products
c. double-sided two page for Overview

2. Pages would be full bleed letter size 8.5” x 11.

3. Samples are included below to get an idea of common grids and layouts for similar publications, as well as one of our current publications for reference.

4. Product literature must include provisions for all of the content types listed in that document, included below. There is some leeway with image placement – a product brochure doesn’t necessarily have to have stock photos, diagrams, AND software screenshots.

5. The designer will need to indicate what specs are required for software screenshots so that we can generate appropriate files for that use.

COMMON ELEMENTS
• Images need to include stock photos of people in business settings, as well as stock photos related to warehousing, barcoding systems, and supply chains. Other images to be used should include schematics, workflow diagrams, and other items that are related to the areas in which the company works. Each heading on the booth, and each page on the brochures, will need one image at minimum. Images and content laid out next to each other should be thematically related whenever possible. We will also create a small number of simple diagrams in house that will need to be redesigned and recreated in the appropriate format and placed in the designs.
• Clean, high-impact design. The Veltrax Tabular Bookkeeping brochure, included below, is a good example of this.
• Our current logo, included below, needs to have the tagline removed. We are also requesting that a different version of the graphic element in the logo be created, in monochrome but with roughly the same geometry.
• Our new tagline is “Integrated Solutions for Ledgerline QP” but it should not be located directly in the logo area as our current tagline is, “Making systems business-ready”.
• Designs should be produced in print-ready PDF files. We will be using Kestrel Layout Pro R4 to open the PDF files, drop in our copy and other content, and finalize the designs. The PDF files will then be sent directly to our booth production and brochure printing companies.

```html
<!DOCTYPE html>
<html lang="en">
<head>
<meta charset="utf-8">
<title>Corvin Meridian – Tradeshow Booth Panels</title>
<link rel="stylesheet" href="https://fonts.googleapis.com/css2?family=Montserrat:wght@600;700;800&display=swap">
<style>
  :root {
    --canvas-grey: #cfcfcf;
    --canvas-grey-light: #e4e4e4;
    --band-white: #ffffff;
    --strip-violet: #5c5a9e;
    --tint-violet: rgba(92, 88, 160, 0.78);
    --tint-violet-soft: rgba(92, 88, 160, 0.0);
    --tagline-grey: #6a6a6a;
    --brand-ink: #3f3f3f;
    --brand-square: #5c5a9e;
    --list-white: #ffffff;
  }
  html, body {
    margin: 0;
    padding: 0;
    width: 1200px;
    height: 363px;
    overflow: hidden;
  }
  body {
    font-family: "Montserrat", Arial, sans-serif;
  }
  .booth {
    position: relative;
    width: 1200px;
    height: 363px;
    overflow: hidden;
    background: linear-gradient(180deg, var(--canvas-grey-light) 0%, var(--canvas-grey) 55%, #bdbdbd 100%);
  }
  .backdrop-pattern {
    position: absolute;
    inset: 0;
    background:
      radial-gradient(ellipse 140px 200px at 40px 240px, rgba(255,255,255,0.35), transparent 70%),
      radial-gradient(ellipse 140px 200px at 600px 240px, rgba(255,255,255,0.3), transparent 70%),
      radial-gradient(ellipse 140px 200px at 1160px 240px, rgba(255,255,255,0.35), transparent 70%);
  }

  /* Vertical category strips */
  .category-strip {
    position: absolute;
    top: 0;
    width: 33px;
    height: 363px;
    background: var(--strip-violet);
  }
  .category-label {
    position: absolute;
    top: 90px;
    left: 0;
    width: 33px;
    writing-mode: vertical-rl;
    transform: rotate(180deg);
    transform-origin: center;
    display: flex;
    align-items: center;
    justify-content: flex-end;
    color: var(--list-white);
    font-weight: 800;
    font-size: 11px;
    letter-spacing: 0.5px;
    line-height: 33px;
    text-transform: uppercase;
    white-space: nowrap;
  }

  /* Photo fields */
  .photo-field {
    position: absolute;
    top: 0;
    height: 363px;
  }
  .photo-field::after {
    content: "";
    position: absolute;
    inset: 0;
    background: linear-gradient(180deg, var(--tint-violet) 0%, var(--tint-violet) 40%, var(--tint-violet-soft) 62%);
  }
  .photo-warehouse {
    left: 138px; width: 182px;
    background: linear-gradient(160deg, #8a7ab0 0%, #a58f78 45%, #c49a63 65%, #3e3f86 100%);
  }
  .photo-workflow {
    left: 353px; width: 192px;
    background: linear-gradient(180deg, #5f7fc0 0%, #4b6fc0 40%, #7fa3dc 70%, #3f63b0 100%);
  }
  .photo-planning {
    left: 688px; width: 180px;
    background: linear-gradient(170deg, #7d72b0 0%, #b8b0d4 45%, #d9dbe8 65%, #4a5aa8 100%);
  }
  .photo-ledger {
    left: 901px; width: 194px;
    background: linear-gradient(180deg, #9fb4d6 0%, #b9cbe3 45%, #d7e2ef 70%, #9fb5d4 100%);
  }

  /* Service lists */
  .service-list {
    position: absolute;
    top: 85px;
    margin: 0;
    padding: 0;
    list-style: none;
    z-index: 2;
  }
  .service-list li {
    color: var(--list-white);
    font-weight: 700;
    font-size: 8px;
    line-height: 17.2px;
    letter-spacing: 0.1px;
    text-transform: uppercase;
    white-space: nowrap;
  }

  /* Header bands */
  .header-band {
    position: absolute;
    top: 16px;
    height: 66px;
    z-index: 3;
  }
  .header-band svg {
    position: absolute;
    inset: 0;
    overflow: visible;
  }
  .band-left { left: 0; width: 580px; }
  .band-right { left: 620px; width: 580px; }
  .header-content {
    position: absolute;
    top: 17px;
    display: flex;
    align-items: center;
    height: 32px;
    white-space: nowrap;
  }
  .brand {
    display: flex;
    align-items: center;
    gap: 5px;
  }
  .brand-square {
    width: 26px;
    height: 26px;
    background: var(--brand-square);
    flex: none;
  }
  .brand-name {
    font-weight: 700;
    font-size: 11.5px;
    color: var(--brand-ink);
    letter-spacing: -0.2px;
    white-space: nowrap;
  }
  .tagline {
    margin-left: 10px;
    font-weight: 600;
    font-size: 12px;
    color: var(--tagline-grey);
    letter-spacing: 0.1px;
    text-transform: uppercase;
    white-space: nowrap;
  }
</style>
</head>
<body>
<main class="booth">
  <div class="backdrop-pattern" role="img" aria-label="Soft grey backdrop with faint light arrow shapes"></div>

  <!-- Left booth half -->
  <div class="photo-field photo-warehouse" role="img" aria-label="Stock photo of a warehouse worker carrying a cardboard box"></div>
  <div class="photo-field photo-workflow" role="img" aria-label="Stock image of a blue workflow diagram with connected boxes and arrows"></div>

  <div class="category-strip" style="left:105px;">
    <span class="category-label" style="height:168px;">WMS/Distribution</span>
  </div>
  <div class="category-strip" style="left:320px;">
    <span class="category-label" style="height:100px;">Workflow</span>
  </div>

  <ul class="service-list" style="left:146px;">
    <li>WMS &amp; Barcode Data Capture</li>
    <li>Catch Weight Handling</li>
    <li>Multi-Dimensional Inventory</li>
    <li>SOP Auto Transfer</li>
    <li>Customer Service Management</li>
  </ul>
  <ul class="service-list" style="left:362px;">
    <li>Document Routing/Approval</li>
    <li>Workflow Tracking &amp; Notifications</li>
    <li>Visual Workflow Designer</li>
    <li>Seamless Integration to QP</li>
    <li>Automated GL Postings</li>
  </ul>

  <header class="header-band band-left">
    <svg width="580" height="66" viewBox="0 0 580 66" aria-hidden="true">
      <polygon points="0,0 548,0 580,33 548,66 0,66" fill="var(--band-white)"/>
    </svg>
    <div class="header-content" style="left:105px;">
      <div class="brand">
        <span class="brand-square"></span>
        <span class="brand-name">Corvin Meridian</span>
      </div>
      <span class="tagline">Integrated Solutions for Ledgerline QP</span>
    </div>
  </header>

  <!-- Right booth half -->
  <div class="photo-field photo-planning" role="img" aria-label="Stock photo of business hands pointing at printed charts on a desk"></div>
  <div class="photo-field photo-ledger" role="img" aria-label="Stock photo of a financial spreadsheet printout with a pen"></div>

  <div class="category-strip" style="left:655px;">
    <span class="category-label" style="height:152px;">Customization</span>
  </div>
  <div class="category-strip" style="left:868px;">
    <span class="category-label" style="height:106px;">Financials</span>
  </div>

  <ul class="service-list" style="left:694px;">
    <li>Quillscript &amp; .Kern Development</li>
    <li>eCommerce Integrations</li>
    <li>Data Modeling &amp; Migrations</li>
    <li>System Re-Engineering</li>
    <li>Custom App Development</li>
  </ul>
  <ul class="service-list" style="left:910px;">
    <li>Credit Card Expense Manager</li>
    <li>Historical Journal Entry</li>
    <li>Balance Brought Forward</li>
    <li>GL Segment Maintenance</li>
    <li>Advanced Customer Merge</li>
  </ul>

  <header class="header-band band-right">
    <svg width="580" height="66" viewBox="0 0 580 66" aria-hidden="true">
      <polygon points="32,0 580,0 580,66 32,66 0,33" fill="var(--band-white)"/>
    </svg>
    <div class="header-content" style="left:33px;">
      <div class="brand">
        <span class="brand-square"></span>
        <span class="brand-name">Corvin Meridian</span>
      </div>
      <span class="tagline">Integrated Solutions for Ledgerline QP</span>
    </div>
  </header>
</main>
</body>
</html>
```